Sponsorship and registration document for Charity Golf Day 2022

The project requires 2 documents to be updated to look more graphically savvy and professionally presentable.
1. Charity golf day sponsorship document
2. One page registration document.
The text has been completed. Text not to be changed - just graphics.
New images would be preferred.
The logos have been provided.

Target Market(s)

Corporate Sponsors and Golf players

Requirements
Must have
• Golf Theme

```html
<!DOCTYPE html>
<html lang="en">
<head>
<meta charset="utf-8">
<title>Charity Golf Day – Sponsorship Proposal</title>
<link href="https://fonts.googleapis.com/css2?family=Arimo:wght@400;700&family=Montserrat:wght@500;600&display=swap" rel="stylesheet">
<style>
:root{
  --blue:#1570b8;
  --green:#8dc63f;
  --lime:#b8d44a;
  --text:#444;
  --muted:#666;
  --bg:#e9e9e9;
  --page:#fff;
}
*{box-sizing:border-box;margin:0;padding:0}
html,body{width:1200px;height:1107px;overflow:hidden;background:var(--bg);font-family:"Arimo",Arial,sans-serif;color:var(--text)}
.spread{position:relative;width:1200px;height:1107px}
.page{position:absolute;width:323px;height:453px;background:var(--page);overflow:hidden;box-shadow:0 2px 6px rgba(0,0,0,.18)}
.p1{left:70px;top:66px}.p2{left:439px;top:66px}.p3{left:807px;top:66px}
.p4{left:70px;top:586px}.p5{left:439px;top:586px}.p6{left:807px;top:586px}

.band{position:absolute;left:13px;top:30px;width:298px;height:16px;display:flex;font-weight:700;font-size:10px;color:#fff;letter-spacing:.2px}
.band .l{background:var(--blue);width:137px;padding-left:13px;line-height:16px}
.band .r{background:var(--green);flex:1;padding-left:18px;line-height:16px}

.footer-wave{position:absolute;right:0;bottom:0;width:155px;height:70px}
.brand{position:absolute;right:10px;bottom:10px;display:flex;align-items:center;gap:3px;text-align:right}
.brand .name{font-size:8px;font-weight:700;color:var(--blue);line-height:1}
.brand .sub{font-size:5px;color:var(--blue);display:block;font-weight:700}
.brand .dot{width:14px;height:14px;border-radius:50%;background:var(--lime)}

/* cover */
.cover-art{position:absolute;left:0;top:0;width:323px;height:320px}
.cover-brand{position:absolute;left:20px;top:20px;font-size:9px;font-weight:700;color:var(--blue);display:flex;align-items:center;gap:3px}
.cover-brand .dot{width:12px;height:12px;border-radius:50%;background:var(--lime)}
.cover-title{position:absolute;left:28px;top:38px;width:215px;text-align:center;color:#fff;font-family:"Montserrat",Arial,sans-serif;text-shadow:0 1px 3px rgba(0,0,0,.35)}
.cover-title .t1{font-size:20px;font-weight:500;letter-spacing:.5px}
.cover-title .t2{font-size:34px;font-weight:500;line-height:1}
.cover-title .t3{font-size:15px;font-weight:500;margin-top:4px}
.cover-title .t4{font-size:7px;margin-top:4px;display:flex;align-items:center;gap:4px;justify-content:center}
.cover-title .t4 i{flex:1;border-top:1px dashed rgba(255,255,255,.8)}
.proposal-pill{position:absolute;left:60px;top:332px;width:206px;height:22px;border:1.2px solid #6aa53a;border-radius:11px;color:var(--green);font-weight:700;font-size:14.5px;text-align:center;line-height:20px}
.cover-sub{position:absolute;left:0;width:323px;top:364px;text-align:center;font-size:7px;line-height:10px;color:var(--muted)}
.cover-url{position:absolute;left:58px;width:282px;top:427px;display:flex;align-items:center;gap:6px;font-size:5.5px;letter-spacing:2px;color:var(--green)}
.cover-url i{flex:1;border-top:.7px solid var(--green)}
.cover-url i:first-child{flex:0 0 55px}.cover-url i:last-child{flex:0 0 55px}

/* contents page */
.label{position:absolute;height:14px;padding:0 6px;color:#fff;font-weight:700;font-size:10px;line-height:14px}
.label.blue{background:var(--blue)}.label.green{background:var(--green)}
.toc{position:absolute;left:25px;top:121px;width:255px;border:.7px solid #9bb8d8;border-collapse:collapse;font-size:6px;color:var(--muted)}
.toc td{border-bottom:.7px solid #9bb8d8;height:14px;padding:0 4px}
.toc td:last-child{text-align:right;width:20px}
.contact{position:absolute;left:29px;top:262px;font-size:6px;line-height:10px;color:var(--text)}
.contact .who{color:var(--blue);font-weight:700}
.contact .k{color:var(--green)}
.contact .gap{height:14px}

/* letter page */
.lead{position:absolute;left:20px;top:70px;width:290px;font-size:9.2px;line-height:12px;color:var(--blue)}
.body{position:absolute;left:20px;width:292px;font-size:5.1px;line-height:9.5px;color:var(--muted)}
.body p{margin-bottom:9px}
.body b{color:var(--text)}
.ticks{list-style:none;margin:4px 0 9px 20px}
.ticks li::before{content:"✓";margin-right:12px;color:var(--muted)}
.sign{width:40px;height:10px;background:linear-gradient(90deg,#d8d0ef,#eeeafa);margin:2px 0 8px}
.sig-name{color:var(--blue);font-weight:700}
.k{color:var(--green)}

/* facts page */
.facts{position:absolute;left:26px;top:56px;width:280px}
.facts h3{font-weight:400;color:var(--blue);font-size:7.2px;margin:0 0 4px 2px}
.squares{list-style:none;margin:0 0 10px 8px;font-size:4.4px;color:var(--muted)}
.squares li{line-height:11px;padding-left:24px;position:relative}
.squares li::before{content:"";position:absolute;left:0;top:4px;width:3px;height:3px;background:#555}
.squares .amt{color:var(--green)}
.squares.tall li{line-height:6.5px;margin-bottom:8px}
.facts p{font-size:4.4px;line-height:8.5px;color:var(--muted);margin-bottom:7px}

/* bronze page */
.tier{position:absolute;left:17px;top:59px;background:var(--blue);color:#fff;font-weight:700;font-style:italic;font-size:10px;padding:0 5px;line-height:12px}
.bronze{position:absolute;left:23px;top:78px;width:285px;font-size:5.1px;color:var(--muted)}
.bronze ul{list-style:none;margin-top:5px}
.bronze li{padding-left:19px;position:relative;line-height:7px;margin-bottom:6px}
.bronze li::before{content:"✓";position:absolute;left:0}
.extra{position:absolute;left:23px;top:198px;font-size:7.5px;color:var(--blue)}
.extra small{font-size:4.6px;color:var(--muted)}
.pay{position:absolute;left:21px;top:224px;background:var(--green);color:#fff;font-size:7.5px;padding:0 3px;line-height:11px}
.pay-grid{position:absolute;left:24px;top:242px;width:280px;font-size:4.8px;color:var(--muted);line-height:10px}
.pay-grid .row{display:flex;margin-bottom:16px}
.pay-grid .h{width:38px;color:var(--blue);font-weight:700}
.pay-grid .k{color:var(--green)}
.box{display:inline-block;width:9px;height:4px;border:.6px solid #777;vertical-align:middle;margin-left:3px}

/* application form */
.form{position:absolute;left:23px;top:66px;width:268px;font-size:5.2px;color:var(--text)}
.form .pkg{font-size:6.8px;color:var(--blue)}
.form .pkg small{font-size:5px}
.opts{display:flex;gap:8px;margin-top:9px;color:var(--green);font-weight:700}
.opts span::before{content:"";display:inline-block;width:9px;height:4px;border:.6px solid #777;margin-right:4px;vertical-align:middle}
.no{text-align:right;margin:6px 45px 0 0;color:var(--text)}
.no::after{content:"";display:inline-block;width:30px;height:4px;border:.6px solid #777;margin-left:3px;vertical-align:middle}
.field{display:flex;line-height:12.6px}
.field b{white-space:nowrap;margin-right:2px}
.field i{flex:1;border-bottom:.7px dotted #888;margin-bottom:4px}
.field .half{flex:0 0 130px}
.team{color:var(--blue);font-size:6.8px;margin:10px 0 4px}
.player{margin-bottom:14px}
.player .field span{font-weight:400}
.note{color:var(--blue);font-size:5.8px}
.note small{color:var(--green);font-size:4.2px}
</style>
</head>
<body>
<main class="spread">

  <!-- Cover -->
  <section class="page p1">
    <svg class="cover-art" viewBox="0 0 323 320" aria-hidden="true">
      <defs>
        <clipPath id="coverClip"><path d="M0 0H323V35C290 90 270 190 200 250 140 300 60 285 0 300Z"/></clipPath>
        <linearGradient id="turf" x1="0" y1="0" x2="0" y2="1">
          <stop offset="0" stop-color="#9fbf6a"/><stop offset=".4" stop-color="#4f8a2a"/><stop offset="1" stop-color="#2f6a1c"/>
        </linearGradient>
      </defs>
      <path d="M0 300C60 285 140 300 200 250 270 190 290 90 323 35V0H323V200C300 250 250 310 170 315 100 320 40 312 0 320Z" fill="#b8d44a"/>
      <path d="M0 305C60 292 140 305 205 262 275 200 300 120 323 60V190C300 250 250 305 170 312 100 318 40 305 0 312Z" fill="#1570b8"/>
      <path d="M0 310C60 300 140 312 205 275 270 220 300 160 323 110V190C300 250 250 300 170 308 100 314 40 302 0 308Z" fill="#8dc63f"/>
      <rect width="323" height="320" fill="url(#turf)" clip-path="url(#coverClip)" role="img" aria-label="Photograph: golf iron resting behind a white ball on a green fairway"/>
    </svg>
    <div class="cover-brand">Fairway Club <span class="dot"></span></div>
    <div class="cover-title">
      <div class="t1">CHARITY</div>
      <div class="t2">GOLF DAY</div>
      <div class="t3">FRIDAY 25 MARCH 2022</div>
      <div class="t4"><i></i>ELMWOOD GOLF CLUB<i></i></div>
    </div>
    <div class="proposal-pill">SPONSORSHIP PROPOSAL</div>
    <div class="cover-sub">Supporting Prostate Cancer Research<br>Help us hit prostate cancer off the green<br>and beat the most common cancer in Australian men</div>
    <div class="cover-url" style="left:58px;width:224px"><i></i>www.fcev.org.au/golf-day<i></i></div>
  </section>

  <!-- Contents -->
  <section class="page p2">
    <div class="band"><span class="l">CHARITY GOLF DAY</span><span class="r">SPONSORSHIP PROPOSAL</span></div>
    <div class="label blue" style="left:23px;top:92px">CONTENTS</div>
    <table class="toc">
      <tr><td>Charity Golf Day Invitation</td><td>2</td></tr>
      <tr><td>About Prostate Cancer</td><td>3</td></tr>
      <tr><td>Why are we asking you to be involved</td><td>3</td></tr>
      <tr><td>What to expect</td><td>4</td></tr>
      <tr><td>Sponsorship Opportunities</td><td>5</td></tr>
      <tr><td>Application Form</td><td>7</td></tr>
    </table>
    <div class="label green" style="left:23px;top:232px">CONTACT</div>
    <div class="contact">
      <div class="who">HELENA (MAROU) PRESTON</div>
      <div class="k">Convenor</div>
      <div><span class="k">Co - </span>President, Fairway Club of Eastvale</div>
      <div><span class="k">Mobile: </span>0400 555 182</div>
      <div><span class="k">Email: </span>helenapreston@mailbox.com</div>
      <div><span class="k">Web: </span>www.fcev.org.au/golf-day</div>
      <div class="gap"></div>
      <div class="who">Clara Benton</div>
      <div class="k">Event Manager</div>
      <div><span class="k">Email: </span>clara.benton@netmail.com</div>
    </div>
    <svg class="footer-wave" viewBox="0 0 155 70" aria-hidden="true"><path d="M0 70C40 30 90 8 155 4V12C100 16 55 40 30 70Z" fill="#1570b8"/><path d="M30 70C55 40 100 18 155 14V24C110 28 75 48 58 70Z" fill="#8dc63f"/><path d="M58 70C75 50 110 32 155 28V40C120 44 95 56 85 70Z" fill="#b8d44a"/></svg>
    <div class="brand"><div><span class="name">Fairway</span><span class="sub">Eastvale</span></div><span class="dot"></span></div>
  </section>

  <!-- Invitation letter -->
  <section class="page p3">
    <div class="band"><span class="l">CHARITY GOLF DAY</span><span class="r">SPONSORSHIP PROPOSAL</span></div>
    <p class="lead">Join us for an exclusive day on the private Elmwood Golf Course, with all proceeds going to support Prostate Cancer Research, Awareness and Support.</p>
    <div class="body" style="top:118px">
      <p>The Fairway Club of Eastvale will again be holding its Charity Golf Day with all proceeds used to support the Prostate Cancer Research, awareness and Support Programs. The venue will be the prestigious Elmwood Golf Club on Friday 25 March 2022, with a shotgun start at 8:00 am.</p>
      <p>We have enclosed for your information a copy of our promotional sponsor packages that outline the event sponsorship package options and inclusions.</p>
      <b>The format of the day involves:</b>
      <ul class="ticks">
        <li>Player registration, refreshments and light breakfast from 7:00am</li>
        <li>Ambrose competition starting at 8:00am</li>
        <li>Two Course lunch and presentations in the club house from 12:30pm</li>
      </ul>
      <p>Your commitment to supporting health programs in our community is truly appreciated. With assistance from sponsors such as yourself, we will continue to see improvements in the support and treatment for men and their families with prostate cancer.</p>
      <p style="margin-top:14px">We hope that you will consider supporting the worthwhile event that is open to any organisation or individual who wishes to enjoy the benefits of playing golf at the prestigious Elmwood Golf Club.</p>
      <p>For more information, please check the website ( www.fcev.org.au/golf-day) or should you wish to discuss any aspect of the event, please contact me on 0400 555 182.</p>
      <b>Yours sincerely</b>
      <div class="sign" role="img" aria-label="Handwritten signature"></div>
      <div style="line-height:7.5px"><span class="sig-name">Helena (Marou) Preston</span><br><span class="k">Convener</span><br><span class="k">Co - </span>President 2021 -2022<br>Secretary 2021 - 2022<br>Fairway Club of Eastvale</div>
    </div>
    <svg class="footer-wave" viewBox="0 0 155 70" aria-hidden="true"><path d="M0 70C40 30 90 8 155 4V12C100 16 55 40 30 70Z" fill="#1570b8"/><path d="M30 70C55 40 100 18 155 14V24C110 28 75 48 58 70Z" fill="#8dc63f"/><path d="M58 70C75 50 110 32 155 28V40C120 44 95 56 85 70Z" fill="#b8d44a"/></svg>
    <div class="brand"><div><span class="name">Fairway</span><span class="sub">Eastvale</span></div><span class="dot"></span></div>
  </section>

  <!-- Prostate cancer facts -->
  <section class="page p4">
    <div class="band"><span class="l">CHARITY GOLF DAY</span><span class="r">SPONSORSHIP PROPOSAL</span></div>
    <div class="facts">
      <h3>Why prostate cancer?</h3>
      <ul class="squares">
        <li>Prostate cancer is the most diagnosed cancer in Australian men.</li>
        <li>Approximately 20,000 Australian men are diagnosed with prostate cancer each year.</li>
        <li>Over 200,000 Australian men are living with a diagnosis prostate cancer.</li>
        <li>95% of Australian men diagnosed with prostate cancer survive for at least 5 years.</li>
        <li>Almost 3,500 Australian men die of prostate cancer each year.</li>
      </ul>
      <h3>Why are we asking you to be involved?</h3>
      <ul class="squares">
        <li>Every day 54 Australian men will be told they have prostate cancer</li>
        <li>70% of research applications are unfunded</li>
        <li>1 in 6 men will suffer from prostate cancer</li>
        <li>9 families lose a loved one to prostate cancer every day</li>
        <li>Only 1 in 3 men have access to a specialist nurse</li>
      </ul>
      <h3 style="margin-left:-2px">What this fundraising event can achieve</h3>
      <ul class="squares tall" style="margin-left:4px">
        <li><span class="amt">$12,500 –</span> Could provide funding for a researcher working for one month on a project to<br>reduce side – effects post treatment.</li>
        <li><span class="amt">$30,000 –</span> could provide finding for a senior scientist for three months working on a project<br>to improve treatments for prostate cancer that has spread to the bones.</li>
        <li><span class="amt">$50,000 –</span> could fund a project to improve early – diagnosis for men with a family history of<br>prostate cancer.</li>
      </ul>
      <p>Proceeds from this event will be donated to Prostate Cancer Research Group at the Health Discovery Institute, Eastern University, to fund world leading, innovative research and to support men and their families affected by prostate cancer.</p>
      <p>Their innovative research program has a strong translational approach, involving lab-based studies with tissues donated by patients with prostate cancer. Their collaborative studies with clinicians and patient advocates address questions that are relevant to patient care. The findings have the potential to improve the management and outcomes of men with different stages of prostate cancer. Recent studies have informed international guidelines for diagnosis of prostate cancer and led to new clinical trials.</p>
      <p>For more information visit their website <b>www.easternuni.edu/discovery/prostate-research-group</b></p>
    </div>
    <svg class="footer-wave" viewBox="0 0 155 70" aria-hidden="true"><path d="M0 70C40 30 90 8 155 4V12C100 16 55 40 30 70Z" fill="#1570b8"/><path d="M30 70C55 40 100 18 155 14V24C110 28 75 48 58 70Z" fill="#8dc63f"/><path d="M58 70C75 50 110 32 155 28V40C120 44 95 56 85 70Z" fill="#b8d44a"/></svg>
    <div class="brand"><div><span class="name">Fairway</span><span class="sub">Eastvale</span></div><span class="dot"></span></div>
  </section>

  <!-- Bronze package -->
  <section class="page p5">
    <div class="band"><span class="l">CHARITY GOLF DAY</span><span class="r">SPONSORSHIP PROPOSAL</span></div>
    <div class="tier">Bronze $650</div>
    <div class="bronze">
      <div>This Bronze Sponsor is entitled to the following:</div>
      <ul>
        <li>Two (2) representatives playing in the event, including all green fees, light breakfast &amp; 2 course lunch</li>
        <li>Exclusive banner with your company logo on a tee</li>
        <li>Your logo and your company information on all promotional and marketing material being used on the day including our website, email to database and our social media channels.</li>
        <li>Great Publicity: Be seen as being associated with an excellent cause</li>
        <li>Opportunity to “capture” prospective clients on the day</li>
        <li>Company merchandising display</li>
        <li>Additional players - $150 per person (including all green fees, light breakfast &amp; 2-course lunch).</li>
      </ul>
    </div>
    <div class="extra">Additional Players - $150 per person - <small>includes all green fees, light breakfast &amp; two (2) course lunch</small></div>
    <div class="pay">PAYMENT OPTIONS:</div>
    <div class="pay-grid">
      <div class="row"><span class="h">By Cheque:</span><span>Please make cheques payable to <span class="k">The Fairway Club of Eastvale</span><br>PO Box 42<br>Northvale, Vic 3100</span></div>
      <div class="row"><span class="h">By Direct<br>Deposit:</span><span><span class="k">Account Name: </span>Fairway Club of Eastvale<br><span class="k">Bank: </span>Harbour Bank<br><span class="k">BSB: </span>100 200<br><span class="k">Account Number: </span>123 456 789<br><span class="k">Comment: </span>FCEGolfDay/your name</span></div>
      <div class="row" style="margin-top:14px"><span class="h">By Credit Card:</span><span style="margin-left:38px">Debit card<span class="box"></span></span><span style="margin-left:30px">Credit card<span class="box"></span></span></div>
      <div style="margin-left:38px;line-height:13px">
        <div>Card No. ____ ____ ____ ______________________ &nbsp; Expiry __/__</div>
        <div>Cardholder’s Name: ..............................................................................................</div>
        <div>Cardholder’s Signature: ............................................................. &nbsp; Date: ..............</div>
      </div>
    </div>
  </section>

  <!-- Application form -->
  <section class="page p6">
    <div class="band"><span class="l">CHARITY GOLF DAY</span><span class="r">APPLICATION FORM</span></div>
    <div class="form">
      <div class="pkg">Sponsorship Package: <small>(Please Tick)</small></div>
      <div class="opts"><span>Gold ($5,000)</span><span>Silver ($2,500)</span><span>Bronze ($650)</span><span>Additional Players ($150)</span></div>
      <div class="no">No:</div>
      <div style="margin-top:4px">
        <div class="field"><b>Company:</b><i></i></div>
        <div class="field"><b>Address:</b><i></i></div>
        <div class="field"><b>Suburb:</b><i></i><b style="margin-left:4px">P/Code:</b><i class="half" style="flex:0 0 55px"></i></div>
        <div class="field"><b>Mobile:</b><i></i></div>
        <div class="field"><b>Contact Name:</b><i></i></div>
        <div class="field"><b>Contact Email:</b><i></i></div>
      </div>
      <div class="team">Team Name:</div>
      <div class="player"><div class="field"><b>Player 1:</b><i></i></div><div class="field"><span>Official GA H/Cap:</span><i class="half"></i><span style="flex:1"></span></div></div>
      <div class="player"><div class="field"><b>Player 2:</b><i></i></div><div class="field"><span>Official GA H/Cap:</span><i class="half"></i><span style="flex:1"></span></div></div>
      <div class="player"><div class="field"><b>Player3:</b><i></i></div><div class="field"><span>Official GA H/Cap:</span><i class="half"></i><span style="flex:1"></span></div></div>
      <div class="player"><div class="field"><b>Player 4:</b><i></i></div><div class="field"><span>Official GA H/Cap:</span><i class="half"></i><span style="flex:1"></span></div></div>
      <div class="note">Please Note: <small>Any player without an official GA H/Cap will be given a maximum handicap of 27 (Males) &amp; 36 (Females)</small></div>
    </div>
  </section>

</main>
</body>
</html>
```